Business Card Design - Local Discount Club

Looking for a fun business card for a local discount club. One side should be the logo only and the other should be have :

Name
Title
Phone, Email
Website

```html
<!DOCTYPE html>
<html lang="en">
<head>
<meta charset="utf-8">
<title>The Harbor Perk Card – Business Card</title>
<link href="https://fonts.googleapis.com/css2?family=Arimo:wght@400;700&display=swap" rel="stylesheet">
<style>
  :root {
    --page: #e4e4e2;
    --card-blue: #3a5bbd;
    --bubble: rgba(255, 255, 255, 0.12);
    --name-blue: #3fa0f0;
    --white: #ffffff;
    --strip-green: #8cf08a;
    --strip-cyan: #3fd3f4;
  }
  * { box-sizing: border-box; margin: 0; padding: 0; }
  html, body {
    width: 1200px; height: 802px; overflow: hidden;
    background: var(--page);
    font-family: "Arimo", Arial, sans-serif;
  }
  .sheet {
    width: 1200px; height: 802px;
    display: flex; align-items: center; justify-content: center; gap: 40px;
  }
  .card {
    position: relative;
    width: 540px; height: 309px;
    background: var(--card-blue);
    overflow: hidden;
    box-shadow: 0 6px 18px rgba(0,0,0,0.18);
  }
  /* Info side */
  .bubble { position: absolute; border-radius: 50%; background: var(--bubble); }
  .bubble--lg { width: 120px; height: 120px; right: 90px; top: 40px; }
  .bubble--md { width: 76px; height: 76px; right: 150px; top: -20px; }
  .bubble--sm { width: 58px; height: 58px; right: 250px; top: 70px; }
  .edge-strip {
    position: absolute; left: 0; right: 0; bottom: 0; height: 9px;
    display: flex;
  }
  .edge-strip__green { flex: 0 0 55%; background: var(--strip-green); }
  .edge-strip__cyan { flex: 1; background: var(--strip-cyan); }
  .brand {
    display: flex; align-items: center; gap: 8px;
    color: var(--white); font-weight: 700;
  }
  .brand__dot { border-radius: 50%; background: var(--strip-cyan); flex: none; }
  .info-side .brand { position: absolute; left: 34px; top: 54px; font-size: 19px; }
  .info-side .brand__dot { width: 12px; height: 12px; }
  .person { position: absolute; left: 34px; top: 128px; }
  .person__name {
    color: var(--name-blue); font-weight: 700; font-size: 19px;
    letter-spacing: 0.5px; text-transform: uppercase;
  }
  .person__title { color: var(--white); font-size: 13px; margin-top: 4px; }
  .contacts { list-style: none; margin-top: 16px; }
  .contacts li {
    display: flex; align-items: center; gap: 9px;
    color: var(--white); font-size: 13.5px; margin-bottom: 6px;
  }
  .contacts svg { width: 13px; height: 13px; flex: none; }
  .address {
    position: absolute; right: 26px; bottom: 28px;
    color: var(--white); font-size: 12.5px; line-height: 1.45; text-align: right;
  }
  /* Logo side */
  .logo-side { display: flex; align-items: center; justify-content: center; }
  .logo-side .brand { font-size: 34px; gap: 12px; }
  .logo-side .brand__dot { width: 20px; height: 20px; }
</style>
</head>
<body>
<main class="sheet">
  <section class="card info-side" aria-label="Business card, contact side">
    <span class="bubble bubble--md"></span>
    <span class="bubble bubble--lg"></span>
    <span class="bubble bubble--sm"></span>

    <div class="brand"><span class="brand__dot"></span>The Harbor Perk Card</div>

    <div class="person">
      <p class="person__name">Morgan Ellery</p>
      <p class="person__title">Manager</p>
      <ul class="contacts">
        <li>
          <svg viewBox="0 0 16 16" aria-hidden="true"><path fill="#fff" d="M3.6 1.5l2.3 2.6-1.2 1.9c.9 2 2.4 3.5 4.4 4.4l1.9-1.2 2.6 2.3-1.3 2.4C7 13.5 2.5 9 1.2 2.8z"/></svg>
          123-456-2100
        </li>
        <li>
          <svg viewBox="0 0 16 16" aria-hidden="true"><rect x="1" y="3" width="14" height="10" fill="#fff"/><path d="M1.5 3.5L8 9l6.5-5.5" fill="none" stroke="#3a5bbd" stroke-width="1.3"/></svg>
          youremail@mailbox.com
        </li>
        <li>
          <svg viewBox="0 0 16 16" aria-hidden="true"><circle cx="8" cy="8" r="6.5" fill="none" stroke="#fff" stroke-width="1.5"/><ellipse cx="8" cy="8" rx="2.6" ry="6.5" fill="none" stroke="#fff" stroke-width="1.2"/><path d="M1.5 8h13" stroke="#fff" stroke-width="1.2"/></svg>
          www.yourwebsite.com
        </li>
      </ul>
    </div>

    <p class="address">Your Address<br>City, State, Zip 0000</p>

    <div class="edge-strip"><span class="edge-strip__green"></span><span class="edge-strip__cyan"></span></div>
  </section>

  <section class="card logo-side" aria-label="Business card, logo side">
    <div class="brand"><span class="brand__dot"></span>The Harbor Perk Card</div>
  </section>
</main>
</body>
</html>
```